50 Lessons from my entrepreneurial journey

make a book cover (see attached file for reference or sample )
https://files.example-share.net/file/d/7kPqWz3rTn8LmYv2XcB5dHj9QsF0aUe4G/view?usp=share_link

make a back book cover (see writings below)

BUILD A BUSINESS. BUILD A LIFE.

What does it really take to succeed, not just in business, but in life?

In MARLO’S LEDGER, award-winning entrepreneur, speaker, and columnist Marlo Dantes shares 50 powerful lessons and more drawn from over three decades of building Cebu’s most beloved homegrown brands. Honest, practical, and deeply personal, this book brings together timeless insights on entrepreneurship, leadership, family, faith, and the inner journey of growth.

Whether you’re just starting out, scaling up, or searching for clarity in the next chapter of your life, these pages will guide, inspire, and challenge you to pursue something greater not just profit, but purpose. More than a business book, this is a book about building the kind of life you won’t need a vacation from.

About the Author

Marlo Dantes is one of Cebu’s most respected and successful entrepreneurs, best known for building iconic homegrown brands such as Breezy Coolers and Blends, Hall of Roastmeat, and The PEAK of Cebu. As Chairman and CEO of the Dantes Food Group, he has spent over 25 years shaping the business landscape of the Visayas and Mindanao. Named Entrepreneur of the Year by the Cebu Guild of Traders and Makers and recognized for one of the Top Ten Most Outstanding Family Businesses in the Philippines, Marlo is also a popular columnist for DayLamp Cebu. Through his writing and mentorship, he continues to empower the next generation to build with heart, lead with purpose, and live with meaning.

Target Market(s)

Millennials & Young Professionals

Industry/Entity Type

Entrepreneurship

Font styles to use
Serif
Sans Serif

Requirements
Must have
• Professional yet clean modern typography

```html
<!DOCTYPE html>
<html lang="en">
<head>
<meta charset="utf-8">
<title>Build a Business. Build a Life. — Cover Spread</title>
<link rel="stylesheet" href="https://fonts.googleapis.com/css2?family=Montserrat:wght@300;400;500;700;800&display=swap">
<style>
  :root {
    --page-bg: #ffffff;
    --ink-dark: #2a2224;
    --panel-dark: #2b2326;
    --spine-dark: #2c2627;
    --paper-light: #c4c2c0;
    --paper-mid: #a9a7a5;
    --accent-yellow: #f2b705;
    --spine-yellow: #f3b43a;
    --white: #ffffff;
  }
  * { margin: 0; padding: 0; box-sizing: border-box; }
  html, body {
    width: 786px; height: 1200px; overflow: hidden;
    background: var(--page-bg);
    font-family: "Montserrat", sans-serif;
  }
  .cover-spread {
    position: absolute; left: 0; top: 316px;
    width: 786px; height: 567px;
    display: flex;
  }
  /* Back cover */
  .back-cover {
    position: relative; width: 377px; height: 100%;
    background: linear-gradient(180deg, var(--paper-light) 0%, #b3b1af 45%, var(--paper-mid) 100%);
    color: var(--ink-dark);
  }
  .back-title {
    position: absolute; left: 0; width: 100%; top: 26px;
    text-align: center;
    font-weight: 800; font-size: 21px; line-height: 28px;
    letter-spacing: -0.3px;
  }
  .back-blurb {
    position: absolute; left: 50px; width: 279px; top: 92px;
    font-size: 10.2px; line-height: 12.2px; font-weight: 400;
  }
  .back-blurb p { text-align: justify; margin-bottom: 12px; }
  .author-panel {
    position: absolute; left: 34px; width: 311px; top: 341px; bottom: 0;
    background: var(--panel-dark);
    color: var(--white);
    padding: 16px 16px 0 16px;
    font-size: 10.2px; line-height: 13.1px;
    text-align: justify;
  }
  .author-panel strong { font-weight: 700; }
  /* Spine */
  .spine {
    position: relative; width: 32px; height: 100%;
    background: var(--spine-dark);
  }
  .spine-text {
    position: absolute; left: 23px; top: 96px;
    transform-origin: 0 0; transform: rotate(90deg);
    white-space: nowrap;
    display: flex; align-items: baseline;
  }
  .spine-title { font-weight: 800; font-size: 14.2px; color: var(--white); }
  .spine-title .accent { color: var(--spine-yellow); }
  .spine-author {
    margin-left: 24px; font-weight: 400; font-size: 8.6px;
    letter-spacing: 1.6px; color: var(--white);
  }
  /* Front cover */
  .front-cover {
    position: relative; width: 377px; height: 100%;
    overflow: hidden;
  }
  .author-portrait {
    position: absolute; inset: 0;
    background:
      radial-gradient(ellipse 45% 35% at 58% 28%, #c9b6a6 0%, rgba(201,182,166,0) 70%),
      linear-gradient(200deg, #d3cdc7 0%, #bdb5ae 38%, #4a4446 62%, #1f1b1c 100%);
  }
  .front-title {
    position: absolute; left: 0; top: 0;
    font-weight: 800; font-size: 36px; line-height: 1;
    color: var(--white);
  }
  .front-title span { position: absolute; white-space: nowrap; }
  .front-title .accent { color: var(--accent-yellow); }
  .line-1 { left: 178px; top: 319px; }
  .line-2 { left: 112px; top: 365px; }
  .line-3 { left: 157px; top: 411px; }
  .line-4 { left: 126px; top: 457px; }
  .front-author {
    position: absolute; left: 52px; top: 528px;
    font-weight: 400; font-size: 16px;
    letter-spacing: 10.4px; color: var(--white);
    white-space: nowrap;
  }
</style>
</head>
<body>
  <main class="cover-spread">
    <section class="back-cover">
      <h2 class="back-title">BUILD A BUSINESS.<br>BUILD A LIFE.</h2>
      <div class="back-blurb">
        <p>What does it really take to succeed, not just in business, but in life?</p>
        <p>In MARLO’S LEDGER, award-winning entrepreneur, speaker, and columnist Marlo Dantes shares 50 powerful lessons and more drawn from over three decades of building Cebu’s most beloved homegrown brands. Honest, practical, and deeply personal, this book brings together timeless insights on entrepreneurship, leadership, family, faith, and the inner journey of growth.</p>
        <p>Whether you’re just starting out, scaling up, or searching for clarity in the next chapter of your life, these pages will guide, inspire, and challenge you to pursue something greater not just profit, but purpose. More than a business book, this is a book about building the kind of life you won’t need a vacation from.</p>
      </div>
      <div class="author-panel">
        <strong>Marlo Dantes</strong> is one of Cebu’s most respected and successful entrepreneurs, best known for building iconic homegrown brands such as Breezy Coolers and Blends, Hall of Roastmeat, and The PEAK of Cebu. As Chairman and CEO of the Dantes Food Group, he has spent over 25 years shaping the business landscape of the Visayas and Mindanao. Named Entrepreneur of the Year by the Cebu Guild of Traders and Makers and recognized for one of the Top Ten Most Outstanding Family Businesses in the Philippines, Marlo is also a popular columnist for DayLamp Cebu. Through his writing and mentorship, he continues to empower the next generation to build with heart, lead with purpose, and live with meaning.
      </div>
    </section>

    <section class="spine">
      <div class="spine-text">
        <span class="spine-title">BUILD A BUSINESS. <span class="accent">BUILD A LIFE.</span></span>
        <span class="spine-author">MARLO’S LEDGER</span>
      </div>
    </section>

    <section class="front-cover">
      <div class="author-portrait" role="img" aria-label="Portrait photograph of the smiling author in glasses, white shirt and dark suit jacket against a light grey studio backdrop"></div>
      <h1 class="front-title">
        <span class="line-1">BUILD</span>
        <span class="line-2">A BUSINESS.</span>
        <span class="line-3 accent">BUILD</span>
        <span class="line-4 accent">A LIFE.</span>
      </h1>
      <p class="front-author">MARLO’S LEDGER</p>
    </section>
  </main>
</body>
</html>
```